Cardiology practice business card

We need a business card for our cardiology practice "Bellmoor Cardiology". We have a new logo, attached below. We like the colours in the logo - red and charcoal. The front of the business card will need to have the doctors name, address, phone number and email. The back will need to have space to write 2 appointment dates and times.

```html
<!DOCTYPE html>
<html lang="en">
<head>
<meta charset="utf-8">
<title>Bellmoor Cardiology — Business Card</title>
<link rel="stylesheet" href="https://fonts.googleapis.com/css2?family=Playfair+Display:wght@400;600&display=swap">
<style>
  :root {
    --red: #c8161d;
    --charcoal: #55575a;
    --ink: #4a4a4a;
    --rule: #9a9a9a;
    --paper: #ffffff;
    --backdrop: #e9e6e1;
    --edge: #d8d8d8;
  }
  * { margin: 0; padding: 0; box-sizing: border-box; }
  html, body { width: 1200px; height: 864px; overflow: hidden; }
  body {
    background: var(--backdrop);
    font-family: "Playfair Display", Georgia, serif;
    display: flex;
    align-items: center;
    justify-content: center;
    gap: 56px;
  }
  .card {
    width: 520px;
    height: 297px;
    background: var(--paper);
    border: 1px solid var(--edge);
    box-shadow: 0 10px 26px rgba(0,0,0,0.12);
    position: relative;
  }
  .card--brand {
    display: flex;
    flex-direction: column;
    align-items: center;
    justify-content: center;
    gap: 34px;
  }
  .wordmark {
    display: flex;
    align-items: center;
    gap: 10px;
    color: var(--red);
    font-weight: 600;
    font-size: 30px;
    letter-spacing: 0.5px;
    white-space: nowrap;
  }
  .wordmark__dot {
    width: 14px; height: 14px;
    border-radius: 50%;
    background: var(--red);
    flex: none;
  }
  .appointments {
    list-style: none;
    color: var(--charcoal);
    font-size: 11px;
    letter-spacing: 0.6px;
    text-transform: uppercase;
  }
  .appointments li {
    display: flex;
    align-items: flex-end;
    gap: 8px;
    margin-top: 12px;
  }
  .appointments__blank {
    display: inline-block;
    border-bottom: 1px solid var(--rule);
    height: 14px;
  }
  .appointments__blank--date { width: 130px; margin-right: 14px; }
  .appointments__blank--time { width: 80px; }

  .card--contact .wordmark {
    position: absolute;
    top: 40px;
    right: 32px;
    font-size: 19px;
    gap: 7px;
  }
  .card--contact .wordmark__dot { width: 10px; height: 10px; }
  .person {
    position: absolute;
    top: 96px;
    left: 40px;
  }
  .person__name {
    color: var(--red);
    font-size: 21px;
    font-weight: 400;
    text-transform: uppercase;
    letter-spacing: 0.3px;
  }
  .person__role {
    color: var(--ink);
    font-size: 18px;
    margin-top: 2px;
  }
  .contact-list {
    position: absolute;
    left: 40px;
    bottom: 18px;
    list-style: none;
    font-size: 8px;
    color: var(--ink);
    text-transform: uppercase;
    line-height: 1.2;
    font-variant-numeric: lining-nums;
  }
  .contact-list li {
    display: flex;
    align-items: center;
    gap: 12px;
    margin-top: 6px;
  }
  .contact-list svg {
    width: 13px; height: 13px;
    fill: none;
    stroke: var(--red);
    stroke-width: 1.5;
    flex: none;
  }
</style>
</head>
<body>
  <section class="card card--brand">
    <div class="wordmark"><span class="wordmark__dot"></span>Bellmoor Cardiology</div>
    <ul class="appointments">
      <li>Date <span class="appointments__blank appointments__blank--date"></span> Time <span class="appointments__blank appointments__blank--time"></span></li>
      <li>Date <span class="appointments__blank appointments__blank--date"></span> Time <span class="appointments__blank appointments__blank--time"></span></li>
    </ul>
  </section>

  <section class="card card--contact">
    <div class="wordmark"><span class="wordmark__dot"></span>Bellmoor Cardiology</div>

    <div class="person">
      <h1 class="person__name">Daniel Harrow</h1>
      <p class="person__role">owner</p>
    </div>

    <ul class="contact-list">
      <li>
        <svg viewBox="0 0 16 16"><rect x="1" y="3" width="14" height="10" rx="1"/><circle cx="5" cy="7" r="1.5"/><path d="M3 11c0-1.5 4-1.5 4 0M9 6h4M9 8h4M9 10h3"/></svg>
        <span>+070 4182 30567<br>+070 4182 30567</span>
      </li>
      <li>
        <svg viewBox="0 0 16 16"><path d="M3 2l3 0 1 3-2 1.5c1 2 2.5 3.5 4.5 4.5L11 9l3 1v3c0 .6-.4 1-1 1C7 14 2 9 2 3c0-.6.4-1 1-1z"/></svg>
        <span>+070 4182 30567<br>+070 4182 30567</span>
      </li>
      <li>
        <svg viewBox="0 0 16 16"><path d="M8 15s5-5 5-8.5A5 5 0 0 0 3 6.5C3 10 8 15 8 15z"/><circle cx="8" cy="6.5" r="1.8"/></svg>
        <span>14 Alder Row<br>Harbour Lane 27</span>
      </li>
      <li>
        <svg viewBox="0 0 16 16"><rect x="1.5" y="3.5" width="13" height="9" rx="1"/><path d="M1.5 4.5l6.5 5 6.5-5"/></svg>
        <span>contact@bellmoorcardio.com</span>
      </li>
      <li>
        <svg viewBox="0 0 16 16"><circle cx="8" cy="8" r="6.5"/><ellipse cx="8" cy="8" rx="3" ry="6.5"/><path d="M1.5 8h13M2.5 4.8h11M2.5 11.2h11"/></svg>
        <span>www.bellmoorcardio.com</span>
      </li>
    </ul>
  </section>
</body>
</html>
```